Business Card Design Project 4 Construction Business

I am after a creative, but sleek and simple/ clean business card design. This design will form the basis of future items and might include a logo or simply a creative way to lay out the text of my company name 'kestrel ventures'
I like the simplicity of black and white however I would also be happy to see a splash of colour introduced somehow to give the text some interest and make it stand out.
I would like a double sided card.
I am young (ish!) and professional, offering construction and project management services, what I don't want is the traditional builders type card featuring a cheesy hammer/ saw image etc.
As the company name, kestrel ventures, suggests, we focus on working closely and collaboratively together, in synergy with all stakeholders involved in the projects that we undertake
Construction

```html
<!DOCTYPE html>
<html lang="en">
<head>
<meta charset="utf-8">
<title>Kestrel Ventures – Business Card</title>
<link rel="stylesheet" href="https://fonts.googleapis.com/css2?family=Michroma&family=Manrope:wght@500;700&display=swap">
<style>
  :root {
    --ink: #1a1a1a;
    --paper: #ffffff;
    --band: #141414;
    --blue: #1b3e94;
    --red: #d4262c;
    --grid: #d9d9d9;
    --page: #ffffff;
  }
  * { margin: 0; padding: 0; box-sizing: border-box; }
  html, body {
    width: 1065px; height: 1200px; overflow: hidden;
    background: var(--page);
  }
  .canvas { position: relative; width: 1065px; height: 1200px; }

  .card {
    position: absolute; left: 0; width: 1065px;
    background: var(--paper);
    border: 2px solid var(--ink);
    overflow: hidden;
  }
  .card--front { top: 0; height: 564px; }
  .card--back { top: 634px; height: 566px; }

  .smallcaps {
    font-family: "Manrope", sans-serif;
    font-weight: 700;
    font-variant: small-caps;
    font-synthesis: small-caps;
  }
  .vertical { writing-mode: vertical-rl; white-space: nowrap; }
  .vertical--up { transform: rotate(180deg); }

  /* Front */
  .brand {
    position: absolute; left: 62px; top: 40px;
    font-family: "Michroma", sans-serif;
    font-size: 40px; line-height: 1.1;
    letter-spacing: 3px;
    color: var(--ink);
    text-transform: uppercase;
  }
  .services {
    position: absolute; left: 34px; top: 476px;
    color: var(--ink); line-height: 1.25;
  }
  .services__line { font-size: 30px; letter-spacing: 8px; }
  .services__line--lead { font-size: 27px; letter-spacing: 4px; }
  .name-band {
    position: absolute; right: 0; top: 0; bottom: 0; width: 57px;
    background: var(--band);
    display: flex; justify-content: center; padding-top: 30px;
  }
  .name-band__name {
    color: var(--paper); font-size: 48px; letter-spacing: 13px;
  }
  .role {
    position: absolute; right: 66px; top: 342px;
    color: var(--blue); font-size: 31px; letter-spacing: 9px;
  }

  /* Back */
  .contact-band {
    position: absolute; left: 0; top: 0; bottom: 0; width: 60px;
    background: var(--band);
    display: flex; justify-content: center; align-items: flex-end; padding-bottom: 120px;
  }
  .contact-band__label {
    font-family: "Manrope", sans-serif; font-weight: 700;
    color: var(--paper); font-size: 36px; letter-spacing: 5px;
  }
  .phone {
    position: absolute; left: 82px; top: 44px; height: 470px;
    display: flex; justify-content: center;
    font-family: "Michroma", sans-serif;
    color: var(--blue); font-size: 27px; letter-spacing: 3px;
  }
  .website {
    position: absolute; left: 152px; top: 10px;
    font-family: "Michroma", sans-serif;
    color: var(--red); font-size: 21px; letter-spacing: 6px;
    text-transform: uppercase;
  }
  .growth-chart { position: absolute; left: 154px; top: 50px; }
  .growth-chart__grid { stroke: var(--grid); stroke-width: 2; fill: none; }
  .growth-chart__axis { stroke: var(--ink); stroke-width: 2.5; fill: none; }
  .growth-chart__line { stroke: var(--red); stroke-width: 3; fill: none; stroke-linejoin: round; }
  .details {
    position: absolute; left: 154px; top: 470px;
    color: var(--ink); font-size: 28px; letter-spacing: 5px; line-height: 43px;
  }
</style>
</head>
<body>
<div class="canvas">

  <section class="card card--front">
    <div class="brand">Kestrel Ventures</div>
    <div class="services smallcaps">
      <div class="services__line services__line--lead">Construction</div>
      <div class="services__line">Project Management Services</div>
    </div>
    <div class="role vertical smallcaps">Director</div>
    <div class="name-band">
      <div class="name-band__name vertical smallcaps">Liam Corrigan</div>
    </div>
  </section>

  <section class="card card--back">
    <div class="contact-band">
      <div class="contact-band__label vertical vertical--up">DETAIL CONTACT</div>
    </div>
    <div class="phone"><span class="vertical vertical--up">PHONE: 0400 555 218</span></div>
    <div class="website">www.kestrelventuresgroup.com.au</div>

    <svg class="growth-chart" width="874" height="402" viewBox="0 0 825 380" role="img" aria-label="Simple rising line chart">
      <g class="growth-chart__grid">
        <path d="M85 0V380M167 0V380M248 0V380M329 0V380M411 0V380M493 0V380M575 0V380M657 0V380M740 0V380M822 0V380"/>
        <path d="M0 2H825M0 49H825M0 96H825M0 143H825M0 190H825M0 238H825M0 285H825M0 332H825"/>
      </g>
      <polyline class="growth-chart__line" points="0,310 85,292 167,282 248,250 329,222 411,205 493,178 575,140 657,110 740,80 822,30"/>
      <path class="growth-chart__axis" d="M1 0V379H825"/>
    </svg>

    <div class="details smallcaps">
      <div>email: liam@kestrelventuresgroup.com.au</div>
      <div>address. 14 Harwood St Lindfield NSW 2070</div>
    </div>
  </section>

</div>
</body>
</html>
```